Label for Gin Bottle - Cranberry & Peach

Hi, We have created a Cranberry & Peach Gin that we require a label for.
The gin will be a vivid Orange/red colour in a clear 50cl bottle
The gin will be 40% Vol.
I am looking for a classy design with a summer/fresh appearance.
Thank You.

```html
<!DOCTYPE html>
<html lang="en">
<head>
<meta charset="utf-8">
<title>Gin Label – Cranberry &amp; Peach</title>
<link href="https://fonts.googleapis.com/css2?family=Ultra&display=swap" rel="stylesheet">
<style>
  :root {
    --leather-dark: #0b0b0b;
    --leather-mid: #2a2a2a;
    --leather-light: #5a5a5a;
    --red-deep: #8e0f10;
    --red-main: #b3181a;
    --gold-light: #fde58a;
    --gold-main: #e1ad2c;
    --gold-dark: #a8721a;
  }
  html, body {
    margin: 0;
    padding: 0;
    overflow: hidden;
    background: #111;
  }
  .label {
    position: relative;
    width: 1200px;
    height: 598px;
    overflow: hidden;
    font-family: "Ultra", Georgia, serif;
    background: linear-gradient(100deg, var(--leather-dark) 0%, var(--leather-mid) 50%, var(--leather-light) 100%);
  }
  .label__art {
    position: absolute;
    inset: 0;
  }
  .gold-text {
    background: linear-gradient(180deg, var(--gold-light) 0%, var(--gold-main) 45%, var(--gold-dark) 70%, var(--gold-light) 100%);
    -webkit-background-clip: text;
    background-clip: text;
    color: transparent;
    margin: 0;
    position: absolute;
    line-height: 1;
    white-space: nowrap;
  }
  .title {
    left: 0;
    right: 0;
    top: 92px;
    text-align: center;
    font-size: 148px;
    letter-spacing: 4px;
  }
  .flavour {
    left: 0;
    right: 0;
    top: 445px;
    text-align: center;
    font-size: 40px;
    letter-spacing: 1px;
  }
  .volume {
    left: 32px;
    top: 540px;
    font-size: 29px;
  }
  .strength {
    right: 30px;
    top: 540px;
    font-size: 29px;
  }
</style>
</head>
<body>
<main class="label">
  <svg class="label__art" width="1200" height="598" viewBox="0 0 1200 598" aria-hidden="false">
    <defs>
      <linearGradient id="red-band" x1="0" y1="0" x2="1" y2="1">
        <stop offset="0" stop-color="#9c1214"/>
        <stop offset="0.5" stop-color="#b3181a"/>
        <stop offset="1" stop-color="#c01e1e"/>
      </linearGradient>
      <linearGradient id="gold-line" x1="0" y1="0" x2="1" y2="0">
        <stop offset="0" stop-color="#a8721a"/>
        <stop offset="0.5" stop-color="#fde58a"/>
        <stop offset="1" stop-color="#a8721a"/>
      </linearGradient>
    </defs>

    <polygon class="band"
      points="0,18 40,10 80,22 120,8 170,20 220,12 260,30 300,15 350,8 400,22 450,10 500,18 560,6 620,20 680,12 740,24 790,14 840,30 900,18 960,38 1010,22 1060,40 1110,26 1160,44 1200,30 1200,300 1150,288 1100,305 1050,290 1000,300 940,285 880,298 820,282 760,296 700,280 640,292 580,278 520,294 460,282 400,300 340,286 280,302 220,288 160,304 100,290 50,306 0,294"
      fill="url(#red-band)" stroke="#e1ad2c" stroke-width="2.5"/>

    <!-- title rules -->
    <line x1="70" y1="162" x2="270" y2="162" stroke="url(#gold-line)" stroke-width="3"/>
    <line x1="915" y1="162" x2="1115" y2="162" stroke="url(#gold-line)" stroke-width="3"/>
    <rect x="272" y="148" width="140" height="28" rx="14" fill="#c8922a" role="img" aria-label="Gold scroll ornament"/>
    <rect x="775" y="148" width="140" height="28" rx="14" fill="#c8922a" role="img" aria-label="Gold scroll ornament"/>

    <!-- flavour rules -->
    <line x1="360" y1="428" x2="840" y2="428" stroke="url(#gold-line)" stroke-width="2"/>
    <line x1="360" y1="500" x2="840" y2="500" stroke="url(#gold-line)" stroke-width="2"/>
    <rect x="520" y="414" width="160" height="20" rx="10" fill="#c8922a" role="img" aria-label="Gold filigree ornament"/>
    <rect x="520" y="494" width="160" height="20" rx="10" fill="#c8922a" role="img" aria-label="Gold filigree ornament"/>
  </svg>

  <h1 class="gold-text title">GIN</h1>
  <p class="gold-text flavour">CRANBERRY &amp; PEACH</p>
  <p class="gold-text volume">50 CL</p>
  <p class="gold-text strength">40% Vol</p>
</main>
</body>
</html>
```